Hi Corinne,

Hope you are well.

I would like you to Design a Lunch Special poster similar to attachment but use my logo and photos instead ( You can reuse the photos from Zest-erific Combo poster )

I prefer if you can start a new FRESH look for the posters so they don't look too similar as previous.

I like to see more YELLOW colour in the poster this time

Thank you

```html
<!DOCTYPE html>
<html lang="en">
<head>
<meta charset="utf-8">
<title>Lunch Special Poster</title>
<link rel="stylesheet" href="https://fonts.googleapis.com/css2?family=Barlow:wght@600;700;800&family=Barlow+Condensed:ital,wght@1,800&display=swap">
<style>
  :root {
    --sun: #fbb731;
    --sun-deep: #f39c12;
    --charcoal: #2f2f31;
    --ink: #3a3a3c;
    --white: #ffffff;
    --cream: #fff6de;
    --shade: rgba(0,0,0,0.35);
  }
  * { box-sizing: border-box; margin: 0; padding: 0; }
  html, body { width: 977px; height: 1200px; overflow: hidden; background: var(--sun); }
  .poster {
    position: relative;
    width: 977px;
    height: 1200px;
    overflow: hidden;
    font-family: "Barlow", sans-serif;
    background: var(--sun);
  }
  .backdrop { position: absolute; inset: 0; width: 977px; height: 1200px; }

  .stamp-panel {
    position: absolute; left: 56px; top: 52px;
    width: 300px; height: 250px;
    background: var(--white);
    border-radius: 28px;
    padding: 22px;
    box-shadow: 0 8px 18px rgba(0,0,0,0.12);
  }
  .stamp-art {
    width: 100%; height: 100%;
    border-radius: 50%;
    background: radial-gradient(ellipse at center, #d14a5c 0%, #c9c4c4 55%, #ececec 100%);
  }

  .brand {
    position: absolute; right: 56px; top: 104px;
    display: flex; align-items: center; gap: 16px;
    color: var(--charcoal);
    font-weight: 800;
    font-size: 40px;
    line-height: 1;
  }
  .brand-dot {
    width: 30px; height: 30px;
    border-radius: 50%;
    background: var(--charcoal);
  }

  .schedule {
    position: absolute; left: 60px; top: 352px;
    color: var(--charcoal);
    font-weight: 700;
    font-size: 72px;
    line-height: 84px;
  }
  .combo-list {
    position: absolute; left: 60px; top: 540px;
    list-style: none;
    color: var(--charcoal);
    font-weight: 600;
    font-size: 31px;
    line-height: 44px;
  }

  .price-disc {
    position: absolute; left: 584px; top: 330px;
    width: 340px; height: 340px;
    border-radius: 50%;
    background: var(--charcoal);
    display: flex; align-items: center; justify-content: center;
  }
  .price {
    color: var(--sun);
    font-family: "Barlow Condensed", sans-serif;
    font-style: italic;
    font-weight: 800;
    font-size: 210px;
    line-height: 1;
    letter-spacing: -3px;
    padding-right: 10px;
  }

  .card {
    position: absolute;
    top: 790px;
    width: 270px; height: 330px;
    background: var(--white);
    padding: 14px;
    box-shadow: 4px 8px 14px var(--shade);
  }
  .card .photo { width: 100%; height: 100%; }
  .card .tag {
    position: absolute; left: 50%; bottom: 30px;
    transform: translateX(-50%);
    width: 86%; height: 48px;
    background: var(--sun);
    color: var(--charcoal);
    font-weight: 700;
    font-size: 28px;
    display: flex; align-items: center; justify-content: center;
    text-transform: uppercase;
  }
  .card-pho { left: 50px; transform: rotate(-5deg); }
  .card-pho .photo { background: linear-gradient(160deg, #6e7a3a, #c9b98a 55%, #4f6a2c); }
  .card-rolls { left: 354px; top: 772px; }
  .card-rolls .photo { background: linear-gradient(180deg, #a9a8a6, #d49a4e 60%, #b57430); }
  .card-drink { left: 657px; transform: rotate(5deg); }
  .card-drink .photo { background: linear-gradient(120deg, #c8202a, #f2f2f2 50%, #1c4f9c 70%, #2a8a3e); }
</style>
</head>
<body>
<main class="poster">
  <svg class="backdrop" viewBox="0 0 977 1200" aria-hidden="true">
    <rect width="977" height="1200" fill="#fbb731"/>
    <circle cx="900" cy="60" r="170" fill="#f39c12"/>
    <path d="M0 740 C220 700 420 770 620 745 C780 725 880 700 977 710 L977 1200 L0 1200 Z" fill="#2f2f31"/>
    <rect x="0" y="1160" width="977" height="40" fill="#fbb731"/>
  </svg>

  <div class="stamp-panel">
    <div class="stamp-art" role="img" aria-label="Round rubber stamp reading Time for Lunch"></div>
  </div>

  <div class="brand"><span class="brand-dot"></span>Basil &amp; Broth</div>

  <h1 class="schedule">Mon-Fri<br>10am-4pm</h1>
  <ul class="combo-list">
    <li>1x Pho (Any Mains)</li>
    <li>1x Springrools (2 only)</li>
    <li>1x Drink (Soft Drink/Water)</li>
  </ul>

  <div class="price-disc"><p class="price">$15</p></div>

  <figure class="card card-pho">
    <div class="photo" role="img" aria-label="Bowl of pho with noodles, beef, herbs and chilli"></div>
    <figcaption class="tag">Pho</figcaption>
  </figure>
  <figure class="card card-rolls">
    <div class="photo" role="img" aria-label="Plate of golden fried spring rolls"></div>
    <figcaption class="tag">Springrools</figcaption>
  </figure>
  <figure class="card card-drink">
    <div class="photo" role="img" aria-label="Two cans of soft drink"></div>
    <figcaption class="tag">Drink</figcaption>
  </figure>
</main>
</body>
</html>
```